Real Estate - Real Estate
Real Estate
Real Estate Company Arrange auction for land selling Real Estate services
- No scrolling - page fit to screen - You need to pick a good arabic font with good colour "If you don't know arabic keep as in photoshop". - This company have no Identity and color theme, its for you to decide - Social media links needed - Arabic interface (Right to left arrangement) - Boss photo attached need to be in the home page. - Welcome message from boss. - Section in the home page for auction announcement "lands auction". - You need to read photoshop layer name to understand the arabic name. - You decide Font colour and type the colour in the photoshop is just for showing. - No field to take any data in the home page.
kiromeltub kiromeltub
Consider it as official website
Graphics - architectural drawings
Please ignore uploaded picture
Please don't focus in Jeddah. Instead focus on "Real Estate" and add some graphics.
I uploaded some picture for jeddah please check it.
This website about jeddah - saudi arabia city only, I will upload some related photo which could be better to use, you pick what you think is better or check with google images.

```html
<!DOCTYPE html>
<html lang="ar" dir="rtl">
<head>
<meta charset="utf-8">
<title>رابطة الأملاك الساحلية</title>
<link href="https://fonts.googleapis.com/css2?family=Aref+Ruqaa:wght@400;700&family=Amiri:wght@400;700&family=Parisienne&family=Open+Sans:ital@0;1&display=swap" rel="stylesheet">
<style>
  :root {
    --night-top: #0d1a3a;
    --night-mid: #27406e;
    --night-low: #1a2440;
    --bar: rgba(10, 18, 44, 0.85);
    --band: rgba(14, 24, 56, 0.72);
    --footer: #0a1230;
    --gold: #e9b43c;
    --gold-soft: #f2c766;
    --white: #ffffff;
    --text-soft: #dfe4f0;
    --social: #3a6fb5;
    --pattern-a: #5a6f96;
    --pattern-b: #2c3d63;
  }
  * { margin: 0; padding: 0; box-sizing: border-box; }
  html, body { width: 1200px; height: 665px; overflow: hidden; background: var(--footer); }
  .page { position: relative; width: 1200px; height: 665px; overflow: hidden; }
  .backdrop {
    position: absolute; inset: 0;
    background: linear-gradient(180deg, var(--night-top) 0%, var(--night-mid) 45%, #3a4d72 62%, var(--night-low) 100%);
  }
  .main-nav {
    position: absolute; top: 0; left: 0; width: 100%; height: 34px;
    background: var(--bar);
    display: flex; flex-direction: row; justify-content: flex-start;
    padding-left: 372px; gap: 46px; align-items: center; direction: ltr;
  }
  .main-nav a {
    font-family: "Parisienne", cursive; font-size: 22px; color: var(--white);
    text-decoration: none; white-space: nowrap;
  }
  .main-nav a.current { color: var(--gold); }
  .pattern { position: absolute; left: 790px; top: 140px; width: 430px; height: 440px; }
  .site-title {
    position: absolute; top: 80px; right: 132px; width: 660px; text-align: center;
    font-family: "Aref Ruqaa", serif; font-weight: 700; font-size: 84px;
    color: var(--gold); line-height: 1.2; white-space: nowrap;
  }
  .boss-photo {
    position: absolute; left: 869px; top: 211px; width: 182px; height: 240px;
    border: 8px solid var(--white);
    background: linear-gradient(180deg, #d9dde4 0%, #b8c0cc 55%, #eef0f3 100%);
  }
  .boss-name {
    position: absolute; top: 290px; right: 372px;
    font-family: "Amiri", serif; font-size: 28px; color: var(--gold-soft); white-space: nowrap;
  }
  .boss-role {
    position: absolute; top: 346px; right: 372px;
    font-family: "Amiri", serif; font-size: 34px; color: var(--white); white-space: nowrap;
  }
  .auction-band {
    position: absolute; left: 0; top: 456px; width: 100%; height: 173px;
    background: var(--band);
  }
  .auction-title {
    position: absolute; left: 600px; top: 462px; direction: ltr; font-weight: 400;
    font-family: "Parisienne", cursive; font-size: 32px; color: var(--gold);
  }
  .auction-text {
    position: absolute; left: 150px; top: 512px; width: 470px; direction: ltr;
    font-family: "Open Sans", sans-serif; font-style: italic; font-size: 13px;
    line-height: 20px; color: var(--text-soft); text-align: right;
  }
  .auction-thumb {
    position: absolute; left: 643px; top: 516px; width: 106px; height: 106px;
    border: 3px solid var(--white);
    background: linear-gradient(160deg, #8fb6e0 0%, #3f6fa8 50%, #24446e 100%);
  }
  .site-footer {
    position: absolute; left: 0; bottom: 0; width: 100%; height: 36px;
    background: var(--footer);
  }
  .copyright {
    position: absolute; left: 749px; top: 10px; direction: ltr;
    font-family: "Open Sans", sans-serif; font-size: 12px; color: var(--text-soft);
  }
  .social { position: absolute; left: 948px; top: 6px; display: flex; gap: 24px; direction: ltr; }
  .social a { display: block; width: 24px; height: 24px; border-radius: 4px; background: var(--social); }
</style>
</head>
<body>
<div class="page">
  <div class="backdrop" role="img" aria-label="Night view of the city waterfront with a lit tower and palm-lined promenade"></div>

  <nav class="main-nav">
    <a href="#">Auction Valuation</a>
    <a href="#">Selling at Auction</a>
    <a href="#">Buying at Auction</a>
    <a href="#">About</a>
    <a href="#" class="current">Home</a>
  </nav>

  <svg class="pattern" viewBox="0 0 430 440" role="img" aria-label="Decorative geometric lattice ornament">
    <defs>
      <linearGradient id="latticeFill" x1="0" y1="0" x2="1" y2="1">
        <stop offset="0" stop-color="#5a6f96" stop-opacity="0.85"/>
        <stop offset="1" stop-color="#2c3d63" stop-opacity="0.7"/>
      </linearGradient>
    </defs>
    <polygon points="215,0 430,220 215,440 0,220" fill="url(#latticeFill)"/>
  </svg>

  <h1 class="site-title">رابطة الأملاك الساحلية</h1>

  <div class="boss-photo" role="img" aria-label="Portrait photo of the chairman"></div>
  <p class="boss-name">فيصل بن ناصر المرزوقي</p>
  <p class="boss-role">رئيس رابطة الأملاك الساحلية</p>

  <section class="auction-band"></section>
  <h2 class="auction-title">Lands Auction</h2>
  <p class="auction-text">Lorem ipsum dolor sit amet, consectetur adipiscing elit. Vestibulum mattis porttitor nulla, eget eleifend metus gravida id. Nunc sollicitudin nunc at tellus pretium a pulvinar purus elementum.</p>
  <div class="auction-thumb" role="img" aria-label="Photo of a modern building for the featured land auction"></div>

  <footer class="site-footer">
    <p class="copyright">Copyright 2014. All right reserved.</p>
    <div class="social">
      <a href="#" aria-label="Social link one"></a>
      <a href="#" aria-label="Social link two"></a>
      <a href="#" aria-label="Social link three"></a>
    </div>
  </footer>
</div>
</body>
</html>
```